Ledgerwise Reach - B2B Demand Generation Website Project

We need a fully functional website for www.ledgerwisereach.example. We are a B2B Demand Generation company, based in London, working with companies such as QRT, VKD, Norvex, Brindlow, Tarvo generating them sales leads for their sales teams. We run this through digital marketing newsletter promotions and have a network of websites. Content syndication, data, demand generation, online marketing. Our logo has just been redone (attached) and we have a holding page already which i would like to use the style / colours. Our logo is bright and vibrant but i dont want the site to be a rainbow. We are expensive, classy, professorial, B2B, intelligent.

Home
About Us
Our Services
Prospora & QA Technology
Intent Data
Testimonials
Contact Us
Updates

Target Market(s)

B2B Marketers (QRT, Velquarion, Tarvo, VKD, Opal Reach, Driftmoor, Harlow Quantis, Technology Companies, Data Companies, Marketing Teams, Tumbleden.

Industry/Entity Type

Marketing

Coding

Coded - Design and coding required

Number of Pages Required

5+ page

Font styles to use
Sans Serif

Requirements
Must have
• Home
About Us
Our Services
Prospora & QA Technology
Intent Data
Testimonials
Contact Us

Simple Pages.

Look classy, intelligent, data experts. I like the video homepages were the image moves at the top. Very soft animation.
Nice to have
• Websites i like:

https://www.vkd.example/
https://www.brevantor.example/
https://www.plumfieldsites.example.co.uk/

Ledgerwise Reach - The Demand Generation Company
Should not have
• Glimpsevault crap images

```html
<!DOCTYPE html>
<html lang="en">
<head>
<meta charset="utf-8">
<title>Ledgerwise Reach - The Demand Generation Company</title>
<link rel="stylesheet" href="https://fonts.googleapis.com/css2?family=Montserrat:wght@300;400;500;600;700;800&display=swap">
<style>
:root{
  --red:#c0272d;
  --blue:#2d6aa8;
  --navy:#0d1a33;
  --navy-deep:#08101f;
  --ink:#2b2b2b;
  --muted:#6b6b6b;
  --line:#e3e3e3;
  --paper:#ffffff;
  --mist:#f0f0f0;
}
*{box-sizing:border-box;margin:0;padding:0}
html,body{width:1200px;height:5177px;overflow:hidden}
body{font-family:'Montserrat',sans-serif;color:var(--ink);background:var(--paper);position:relative}
.section{position:absolute;left:0;width:1200px}
.abs{position:absolute}
.photo{position:absolute}

/* brand */
.brand{display:flex;align-items:center;gap:12px}
.brand-dot{width:46px;height:46px;border-radius:50%;border:4px solid var(--red)}
.brand-name{font-weight:500;font-size:27px;color:var(--red);letter-spacing:-.5px}

/* headings */
.h-split{font-weight:300;font-size:38px;line-height:42px;color:var(--ink)}
.h-split b{font-weight:800;color:var(--red)}
.marker{display:flex;align-items:center;gap:0;margin-top:20px}
.marker i{width:22px;height:22px;border-radius:50%;border:5px solid #f1c9cb;background:var(--paper);box-shadow:inset 0 0 0 3px var(--red)}
.marker span{display:block;width:150px;height:1px;background:var(--line);margin-left:8px}
.dark .marker span{background:rgba(255,255,255,.2)}
.dark .marker i{background:transparent;border-color:rgba(192,39,45,.35)}

.body-text{font-size:14px;line-height:21px;letter-spacing:.4px;color:#333}

/* learn more */
.btn{display:flex;align-items:center;gap:12px;width:180px;height:34px;background:var(--paper);box-shadow:0 3px 10px rgba(0,0,0,.12);padding-left:10px;font-size:10px;font-weight:700;letter-spacing:1px;color:var(--ink)}
.btn .arrow{width:18px;height:18px;border-radius:50%;border:1.5px solid var(--red);display:flex;align-items:center;justify-content:center}
.btn .slash{width:1px;height:18px;background:#bbb;transform:rotate(25deg)}

/* hero */
.hero{top:0;height:635px;overflow:hidden}
.hero .photo{inset:0;background:radial-gradient(ellipse at 70% 40%,#3c5a86 0%,#1a2c4e 45%,#0a1426 100%)}
.hero .brand{position:absolute;left:70px;top:40px}
.burger{position:absolute;left:1093px;top:56px;width:36px}
.burger span{display:block;height:3px;background:#fff;margin-bottom:7px}
.burger span:nth-child(2){width:26px;margin-left:10px}
.hero-title{position:absolute;left:106px;top:210px;color:#fff;font-size:56px;line-height:57px;font-weight:300;text-transform:uppercase}
.hero-title b{font-weight:800}

.stats{top:543px;left:106px;width:987px;height:156px;background:var(--blue);display:flex;align-items:center;padding-left:44px;gap:0;box-shadow:0 10px 30px rgba(0,0,0,.2)}
.stat{display:flex;align-items:center;gap:14px;width:326px}
.stat-num{font-size:44px;font-weight:300;color:#fff;line-height:44px}
.stat-label{font-size:11px;font-weight:600;color:#fff;letter-spacing:.5px;margin-top:4px}

/* intro */
.intro{top:700px;height:606px}
.frame{position:absolute;border:1px solid var(--line)}

/* clients */
.clients{top:1306px;height:358px;background:radial-gradient(ellipse at 85% 60%,#24406e 0%,#112241 45%,#0a1528 100%)}
.client{position:absolute;width:182px;height:96px;background:rgba(40,70,115,.55);display:flex;align-items:center;justify-content:center;color:rgba(255,255,255,.85);font-weight:600;font-size:20px;letter-spacing:1px}

/* leads */
.leads{top:1664px;height:606px}

/* services */
.services{top:2270px;height:599px;color:#fff}
.services .photo{inset:0;background:radial-gradient(ellipse at 30% 40%,#1f3a5e 0%,#0f1f38 50%,#060d1a 100%)}
.sec-title{position:absolute;width:1200px;text-align:center;font-size:38px;font-weight:300;color:#fff}
.sec-title b{font-weight:800}
.card{position:absolute;top:196px;width:330px;height:326px;background:rgba(10,22,42,.75);text-align:center;padding:34px 34px 0}
.card svg{display:block;margin:0 auto 28px}
.card h3{font-size:14px;font-weight:700;line-height:20px;letter-spacing:.5px}
.card p{font-size:13px;line-height:18px;color:rgba(255,255,255,.6);margin-top:14px;letter-spacing:.4px}
.card .btn{position:absolute;left:89px;top:278px;width:152px}

/* tech */
.tech{top:2869px;height:626px}
.product{position:absolute;left:80px;top:224px;display:flex;flex-direction:column;align-items:center;gap:14px}
.product-mark{width:58px;height:58px;border-radius:50%;border:4px solid #d4a14a}
.product-name{font-size:34px;font-weight:400;letter-spacing:6px;color:#333}

/* intent */
.intent{top:3495px;height:410px}
.intent .photo{inset:0;background:radial-gradient(ellipse at 70% 50%,#4a1e26 0%,#1b2338 40%,#0a1222 100%)}
.intent p{position:absolute;left:127px;width:946px;top:197px;text-align:center;font-size:14px;line-height:21px;color:rgba(255,255,255,.75);letter-spacing:.4px}

/* testimonials */
.testi{top:3905px;height:604px}
.person{position:absolute;left:753px;top:313px;display:flex;align-items:center;gap:20px}
.avatar{width:86px;height:86px;border-radius:50%;background:linear-gradient(135deg,#e6cfb0,#b99a7a);border:5px solid #fff;box-shadow:0 4px 12px rgba(0,0,0,.15)}

/* contact bar */
.contact-bg{top:4590px;height:587px;background:var(--mist)}
.contact{top:4509px;left:106px;width:987px;height:157px;background:var(--blue);display:flex;align-items:center;color:#fff}
.c-item{display:flex;align-items:flex-start;gap:18px}
.c-label{font-size:11px;font-weight:600;letter-spacing:.8px;opacity:.85}
.c-val{font-size:14px;font-weight:600;line-height:20px;margin-top:3px}

/* footer */
.foot-brand{top:4716px;left:0;width:1200px;display:flex;flex-direction:column;align-items:center;gap:10px}
.foot-brand .brand-dot{width:62px;height:62px}
.tagline{font-size:10px;color:var(--blue);letter-spacing:.5px}
.col{position:absolute;top:4871px}
.col h4{font-size:11px;font-weight:700;color:var(--blue);letter-spacing:.8px;padding-bottom:8px;border-bottom:1px solid #d3d3d3;width:150px;margin-bottom:12px}
.col li{list-style:none;font-size:10px;line-height:15px;font-weight:500;color:#333}
.col .ci{display:flex;gap:8px;font-size:10px;line-height:15px;font-weight:500;margin-bottom:12px}
.subscribe{display:flex;margin-top:4px}
.subscribe span{width:130px;height:28px;border:1px solid #ccc;background:#fff;font-size:10px;padding:7px 8px;font-weight:500}
.subscribe b{width:28px;height:28px;border:1px solid #ccc;border-left:0;background:#fff;display:flex;align-items:center;justify-content:center}
.legal{position:absolute;top:5097px;left:760px;font-size:8px;letter-spacing:.6px;color:#888;line-height:14px}
.social{position:absolute;top:5098px;left:151px;display:flex;gap:14px}
.social i{width:12px;height:12px;border-radius:50%;background:#aab}
</style>
</head>
<body>

<!-- HERO -->
<header class="section hero">
  <div class="photo" role="img" aria-label="Businessman touching a holographic data dashboard with charts"></div>
  <div class="brand"><span class="brand-dot"></span><span class="brand-name">Ledgerwise Reach</span></div>
  <div class="burger"><span></span><span></span><span></span></div>
  <h1 class="hero-title">We deliver<br>your <b>demand<br>generation<br>strategy</b></h1>
</header>

<div class="section stats">
  <div class="stat">
    <svg width="50" height="50" viewBox="0 0 50 50" fill="none" stroke="#fff" stroke-width="4"><path d="M14 8H6v36h38V8h-8"/><path d="M25 4v24M15 19l10 10 10-10"/></svg>
    <div><div class="stat-num">70,000+</div><div class="stat-label">DOWNLOADS PER MONTH</div></div>
  </div>
  <div class="stat">
    <svg width="56" height="50" viewBox="0 0 56 50" fill="#fff"><path d="M4 18h10l20-12v38L14 32H4z"/><rect x="10" y="32" width="8" height="12"/><path d="M40 14l8-4M40 25h10M40 36l8 4" stroke="#fff" stroke-width="3"/></svg>
    <div><div class="stat-num">25,000+</div><div class="stat-label">LEADS DELIVERED PER MONTH</div></div>
  </div>
  <div class="stat">
    <svg width="54" height="54" viewBox="0 0 54 54" fill="none" stroke="#fff" stroke-width="4"><circle cx="27" cy="27" r="23"/><path d="M10 18c8 2 10 8 16 8s6 10 2 16M34 8c-2 6 4 10 12 10"/></svg>
    <div><div class="stat-num">50+</div><div class="stat-label">COUNTRIES WE CAN REACH</div></div>
  </div>
</div>

<!-- INTRO -->
<section class="section intro">
  <div class="frame" style="left:580px;top:96px;width:620px;height:430px"></div>
  <div class="photo" role="img" aria-label="Businessman looking over a futuristic city skyline" style="left:599px;top:90px;width:601px;height:424px;background:linear-gradient(135deg,#8aa0bd,#3f5676 55%,#1d2a40)"></div>
  <div class="abs" style="left:540px;top:50px;width:488px;height:180px;background:#fff"></div>
  <div class="abs" style="left:566px;top:74px">
    <h2 class="h-split">Multi-Channel <b>Demand<br>Generation Services</b></h2>
    <div class="marker"><i></i></div>
  </div>
  <p class="abs body-text" style="left:72px;top:215px;width:445px">Ledgerwise Reach offers multi-channel demand generation services to publishers and technology vendors through our network of lead generation websites and native speaking telemarketing agents. Whether looking for MQL, ABM or BANT campaigns, Ledgerwise Reach can assist you in delivering your demand generation strategy and generate pipeline for your sales teams and/or channel partners.</p>
  <div class="abs btn" style="left:72px;top:410px"><span class="arrow"><svg width="8" height="8" viewBox="0 0 8 8" fill="none" stroke="#c0272d" stroke-width="1.5"><path d="M1 4h6M4 1l3 3-3 3"/></svg></span><span class="slash"></span>LEARN MORE</div>
</section>

<!-- CLIENTS -->
<section class="section clients">
  <div class="photo" role="img" aria-label="Faint globe with network lines" style="left:760px;top:40px;width:420px;height:300px;background:radial-gradient(circle,rgba(90,120,170,.35),transparent 70%)"></div>
  <div class="client" style="left:106px;top:72px">QRT</div>
  <div class="client" style="left:307px;top:72px">Tarvo</div>
  <div class="client" style="left:508px;top:72px">VKD</div>
  <div class="client" style="left:709px;top:72px">Halden</div>
  <div class="client" style="left:910px;top:72px">Nimbrel</div>
  <div class="client" style="left:106px;top:189px">Corvane</div>
  <div class="client" style="left:307px;top:189px">Shiftwell</div>
  <div class="client" style="left:508px;top:189px">Quillon</div>
  <div class="client" style="left:709px;top:189px">Sellmark</div>
</section>

<!-- LEADS -->
<section class="section leads">
  <div class="photo" role="img" aria-label="Abstract data bars with glowing circles" style="left:0;top:94px;width:152px;height:180px;background:linear-gradient(135deg,#7c96b8,#2b4466)"></div>
  <div class="frame" style="left:6px;top:278px;width:616px;height:250px"></div>
  <div class="photo" role="img" aria-label="Team of colleagues reviewing work at a computer" style="left:0;top:268px;width:599px;height:248px;background:linear-gradient(120deg,#4c6a8c,#223650 60%,#141f30)"></div>
  <div class="abs" style="left:152px;top:50px;width:470px;height:218px;background:#fff"></div>
  <div class="abs" style="left:195px;top:74px">
    <h2 class="h-split">We Deliver High-Quality<br><b>Sales Leads</b> from any<br>country in the world</h2>
    <div class="marker"><i></i><span></span></div>
  </div>
  <p class="abs body-text" style="left:717px;top:256px;width:420px">Ledgerwise Reach offer expert demand generation support, from providing detailed leads of qualified decision-makers, to a comprehensive lead generation and SQL service.</p>
  <p class="abs body-text" style="left:717px;top:361px;width:420px">With access to over 31 million names, Ledgerwise Reach offers a range of marketing options that allow you to use our data to target the decision makers you need to reach.</p>
  <div class="abs btn" style="left:717px;top:470px"><span class="arrow"><svg width="8" height="8" viewBox="0 0 8 8" fill="none" stroke="#c0272d" stroke-width="1.5"><path d="M1 4h6M4 1l3 3-3 3"/></svg></span><span class="slash"></span>LEARN MORE</div>
</section>

<!-- SERVICES -->
<section class="section services dark">
  <div class="photo" role="img" aria-label="Dark blue abstract dotted wave background"></div>
  <h2 class="sec-title" style="top:72px">Our <b>Services</b></h2>
  <div class="abs" style="left:477px;top:126px"><div class="marker" style="margin-top:0"><i></i><span></span></div></div>

  <div class="card" style="left:70px">
    <svg width="70" height="56" viewBox="0 0 70 56" fill="none" stroke="#3f7fc4" stroke-width="2.5"><rect x="6" y="6" width="40" height="28"/><path d="M20 34v10h12M18 44h16"/><rect x="42" y="18" width="20" height="32"/><circle cx="26" cy="20" r="6"/></svg>
    <h3>Marketing Qualified Leads<br>(MQL)</h3>
    <p>A Marketing Qualified Lead (MQL) is a prospect that has expressed an interest in what your brand has to offer.</p>
    <div class="btn"><span class="arrow"><svg width="8" height="8" viewBox="0 0 8 8" fill="none" stroke="#c0272d" stroke-width="1.5"><path d="M1 4h6M4 1l3 3-3 3"/></svg></span><span class="slash"></span>LEARN MORE</div>
  </div>
  <div class="card" style="left:434px">
    <svg width="70" height="56" viewBox="0 0 70 56" fill="none" stroke="#3f7fc4" stroke-width="2.5"><rect x="18" y="4" width="44" height="30"/><rect x="6" y="18" width="36" height="26"/><path d="M24 44v8M14 52h20"/></svg>
    <h3>Account Based Marketing Leads<br>(ABM)</h3>
    <p>ABM is a strategy that directs marketing resources to engaging a specific set of target accounts.</p>
    <div class="btn"><span class="arrow"><svg width="8" height="8" viewBox="0 0 8 8" fill="none" stroke="#c0272d" stroke-width="1.5"><path d="M1 4h6M4 1l3 3-3 3"/></svg></span><span class="slash"></span>LEARN MORE</div>
  </div>
  <div class="card" style="left:798px">
    <svg width="70" height="56" viewBox="0 0 70 56" fill="none" stroke="#3f7fc4" stroke-width="2.5"><path d="M6 22h8l14-10v32L14 34H6z"/><path d="M34 28h12M46 10v36M46 10h10M46 22h10M46 34h10M46 46h10"/><circle cx="60" cy="10" r="3"/><circle cx="60" cy="22" r="3"/><circle cx="60" cy="34" r="3"/><circle cx="60" cy="46" r="3"/></svg>
    <h3>Sales Qualified Lead / BAN</h3>
    <p>An SQL lead or a BANT lead is a type of lead that expressed a specific interest in a product and service that you have to offer</p>
    <div class="btn"><span class="arrow"><svg width="8" height="8" viewBox="0 0 8 8" fill="none" stroke="#c0272d" stroke-width="1.5"><path d="M1 4h6M4 1l3 3-3 3"/></svg></span><span class="slash"></span>LEARN MORE</div>
  </div>
</section>

<!-- TECH -->
<section class="section tech">
  <div class="frame" style="left:580px;top:240px;width:620px;height:170px"></div>
  <div class="photo" role="img" aria-label="Businessman holding a tablet with a rising bar chart" style="left:599px;top:234px;width:601px;height:284px;background:linear-gradient(135deg,#9eb3cb,#48607f 55%,#1b2638)"></div>
  <div class="photo" role="img" aria-label="Businessman in a dark suit" style="left:960px;top:90px;width:240px;height:150px;background:linear-gradient(180deg,#4a5568,#1f2633)"></div>
  <div class="abs" style="left:540px;top:74px;width:420px;height:170px;background:#fff"></div>
  <div class="abs" style="left:566px;top:90px">
    <h2 class="h-split"><b>Prospora and QA</b><br>Technology</h2>
    <div class="marker"><i></i><span></span></div>
  </div>
  <div class="product"><span class="product-mark"></span><span class="product-name">PROSPORA</span></div>
  <p class="abs body-text" style="left:72px;top:364px;width:450px">Prospora is a proprietary lead verification platform from Ledgerwise Reach that aims to sift out invalid leads with questionable or erroneous data. The platform is designed to equip sales teams with accurate, high-quality records in order to improve lead generation, accelerate pipeline and increase revenue.</p>
  <div class="abs btn" style="left:72px;top:530px"><span class="arrow"><svg width="8" height="8" viewBox="0 0 8 8" fill="none" stroke="#c0272d" stroke-width="1.5"><path d="M1 4h6M4 1l3 3-3 3"/></svg></span><span class="slash"></span>LEARN MORE</div>
</section>

<!-- INTENT -->
<section class="section intent dark">
  <div class="photo" role="img" aria-label="Dark network of connected red nodes"></div>
  <h2 class="sec-title" style="top:76px">Intent <b style="color:#3f7fc4;font-weight:700">Data</b></h2>
  <div class="abs" style="left:490px;top:132px"><div class="marker" style="margin-top:0"><i></i><span></span></div></div>
  <p>Our relationships with the world's most important technology &amp; business decisions-makers generate a perpetual stream of global data. With access to 35 million individuals and a global behavioural data stream that is authenticated, timely and contextually relevant, we have one of the industry's most powerful signals of buyer intent and can fuel your demand-generation marketing strategies globally.</p>
  <div class="abs btn" style="left:510px;top:300px"><span class="arrow"><svg width="8" height="8" viewBox="0 0 8 8" fill="none" stroke="#c0272d" stroke-width="1.5"><path d="M1 4h6M4 1l3 3-3 3"/></svg></span><span class="slash"></span>LEARN MORE</div>
</section>

<!-- TESTIMONIALS -->
<section class="section testi">
  <div class="frame" style="left:6px;top:120px;width:616px;height:410px"></div>
  <div class="photo" role="img" aria-label="Group of colleagues discussing work around a table" style="left:0;top:84px;width:599px;height:424px;background:linear-gradient(120deg,#8a7a68,#5e5145 50%,#3a332c)"></div>
  <div class="abs" style="left:188px;top:60px;width:430px;height:150px;background:#fff"></div>
  <div class="abs" style="left:267px;top:84px">
    <h2 class="h-split"><b>Client</b> Testimonials</h2>
    <div class="marker"><i></i><span></span></div>
  </div>
  <p class="abs body-text" style="left:753px;top:158px;width:380px">Lorem ipsum dolor sit amet, consectetur adipiscing elit, sed do eismod tempor incididunt ut labore et do lore magna aliqua. Ut en im ad minim veniam, quis nostrud exercitation ullamco laboris nisi ut aliqu ip ex ea commodo consequat.</p>
  <div class="person">
    <div class="avatar" role="img" aria-label="Client portrait"></div>
    <div><div style="font-weight:700;font-size:15px">Maren Hollis</div><div style="font-size:14px;color:var(--muted)">Fernway UK</div></div>
  </div>
  <svg class="abs" style="left:1068px;top:350px" width="44" height="16" viewBox="0 0 44 16" fill="none" stroke="#14306a" stroke-width="3"><path d="M8 2L2 8l6 6M36 2l6 6-6 6"/></svg>
</section>

<!-- CONTACT -->
<div class="section contact-bg"></div>
<div class="section contact">
  <div class="c-item" style="margin-left:98px;width:230px">
    <svg width="40" height="40" viewBox="0 0 40 40" fill="#fff"><path d="M8 3l7 8-4 5c3 6 7 10 13 13l5-4 8 7-5 6C18 36 4 22 2 8z"/></svg>
    <div><div class="c-label">CALL US</div><div class="c-val">+442070001234</div></div>
  </div>
  <div class="c-item" style="width:314px">
    <svg width="40" height="40" viewBox="0 0 40 40" fill="#fff"><path d="M38 2L2 18l12 5 3 13 6-8 9 6z"/></svg>
    <div><div class="c-label">EMAIL US</div><div class="c-val">hello@ledgerwisereach.example</div></div>
  </div>
  <div class="c-item">
    <svg width="30" height="42" viewBox="0 0 30 42" fill="#fff"><path d="M15 0C7 0 1 6 1 14c0 10 14 28 14 28s14-18 14-28C29 6 23 0 15 0zm0 20a6 6 0 110-12 6 6 0 010 12z"/></svg>
    <div><div class="c-label">OFFICE</div><div class="c-val">Quayside Lane 42<br>London, England EC9 4ZZ, GB</div></div>
  </div>
</div>

<!-- FOOTER -->
<footer>
  <div class="section foot-brand">
    <span class="brand-dot"></span>
    <span class="brand-name">Ledgerwise Reach</span>
    <span class="tagline">The Demand Generation Company</span>
  </div>
  <div class="col" style="left:151px">
    <h4>NAVIGATION</h4>
    <ul><li>Home</li><li>About Us</li><li>Our Services</li><li>Prospora &amp; QA Technology</li><li>Intent Data</li><li>Testimonials</li><li>Contact</li></ul>
  </div>
  <div class="col" style="left:362px">
    <h4>SERVICES</h4>
    <ul><li>Marketing Qualified Leads (MQL)</li><li>Account Based Marketing Leads (ABM)</li><li>Sales Qualified Lead / BANT</li></ul>
  </div>
  <div class="col" style="left:659px">
    <h4>CONTACT</h4>
    <div class="ci"><svg width="8" height="11" viewBox="0 0 30 42" fill="#c0272d"><path d="M15 0C7 0 1 6 1 14c0 10 14 28 14 28s14-18 14-28C29 6 23 0 15 0z"/></svg><span>Ledgerwise Reach<br>Quayside Lane<br>42<br>London, England EC9 4ZZ, GB</span></div>
    <div class="ci"><svg width="10" height="10" viewBox="0 0 40 40" fill="#c0272d"><path d="M8 3l7 8-4 5c3 6 7 10 13 13l5-4 8 7-5 6C18 36 4 22 2 8z"/></svg><span>+442070001234</span></div>
    <div class="ci"><svg width="10" height="8" viewBox="0 0 10 8" fill="#c0272d"><rect width="10" height="8"/></svg><span>hello@ledgerwisereach.example</span></div>
  </div>
  <div class="col" style="left:896px">
    <h4>SIGN UP FOR THE LATEST</h4>
    <div class="subscribe"><span>Email Address</span><b><svg width="10" height="10" viewBox="0 0 8 8" fill="none" stroke="#333" stroke-width="1.2"><path d="M1 4h6M4 1l3 3-3 3"/></svg></b></div>
  </div>
  <div class="social"><i></i><i></i><i></i><i></i></div>
  <div class="legal">PRIVACY POLICY &nbsp;|&nbsp; COOKIE POLICY &nbsp;|&nbsp; DATA USAGE POLICY<br>© 2020 LEDGERWISE REACH - ALL RIGHTS RESERVED</div>
</footer>

</body>
</html>
```